Presentation Folder, Business Card, Letterhead and Envelope design

We are a dental clinic that will open in August and we are looking for a professional graphic designer to create our Business Card, Presentation Folder, Letterhead, Notepad and envelopes.

The brand LumaGrin must reflect a sense of quality and sophistication, marketed for middle-class consumers.
Our preference is for quality and refined materials, where less is more.
Attached the logo

```html
<!DOCTYPE html>
<html lang="en">
<head>
<meta charset="utf-8">
<title>LumaGrin Business Card</title>
<link rel="stylesheet" href="https://fonts.googleapis.com/css2?family=Raleway:wght@700&family=Roboto:wght@300;400&display=swap">
<style>
  :root {
    --backdrop: #9a9a9a;
    --card-white: #ffffff;
    --ink-grey: #555555;
    --brand-maroon: #6e1417;
    --band-grey: #5a5a5a;
    --front-light: #5c5c5c;
    --front-dark: #0d0d0d;
  }
  * { margin: 0; padding: 0; box-sizing: border-box; }
  html, body {
    width: 1101px;
    height: 1200px;
    overflow: hidden;
    background: var(--backdrop);
  }
  .card {
    position: absolute;
    left: 185px;
    width: 742px;
    height: 412px;
  }
  .card-front {
    top: 130px;
    background: #151515;
    padding: 18px;
  }
  .front-pattern {
    width: 100%;
    height: 100%;
    background: linear-gradient(90deg, var(--front-light) 0%, #2a2a2a 50%, var(--front-dark) 100%);
  }
  .card-back {
    top: 630px;
    background: var(--card-white);
    font-family: "Roboto", Arial, sans-serif;
    color: var(--ink-grey);
  }
  .brand {
    position: absolute;
    left: 345px;
    top: 56px;
    display: flex;
    align-items: center;
    gap: 12px;
  }
  .brand-square {
    width: 40px;
    height: 40px;
    background: var(--ink-grey);
  }
  .brand-name {
    font-weight: 300;
    font-size: 36px;
    letter-spacing: 0.28em;
    color: var(--ink-grey);
    line-height: 1;
  }
  .name-marker {
    position: absolute;
    left: 0;
    top: 206px;
    width: 20px;
    height: 45px;
    background: var(--brand-maroon);
  }
  .holder-name {
    position: absolute;
    left: 59px;
    top: 203px;
    font-family: "Raleway", Arial, sans-serif;
    font-weight: 700;
    font-size: 24px;
    color: var(--brand-maroon);
    line-height: 1.2;
  }
  .holder-title {
    position: absolute;
    left: 59px;
    top: 229px;
    font-size: 21px;
    line-height: 1.2;
  }
  .contact-list {
    position: absolute;
    left: 59px;
    top: 273px;
    list-style: none;
    font-size: 22px;
    line-height: 28.5px;
  }
  .contact-item {
    display: flex;
    align-items: center;
    gap: 6px;
  }
  .contact-icon {
    width: 21px;
    height: 21px;
    fill: var(--brand-maroon);
  }
  .address {
    position: absolute;
    right: 66px;
    top: 302px;
    text-align: right;
    font-size: 22px;
    line-height: 28.5px;
    font-style: normal;
  }
  .footer-band {
    position: absolute;
    left: 0;
    bottom: 0;
    width: 742px;
    height: 13px;
  }
</style>
</head>
<body>
  <section class="card card-front">
    <div class="front-pattern" role="img" aria-label="Embossed grid of tiles fading from grey to black with one highlighted silver and maroon tile"></div>
  </section>

  <section class="card card-back">
    <div class="brand">
      <span class="brand-square"></span>
      <span class="brand-name">LUMAGRIN</span>
    </div>

    <span class="name-marker"></span>
    <h1 class="holder-name">DANIEL WHITCOMBE</h1>
    <p class="holder-title">Managing Director</p>

    <ul class="contact-list">
      <li class="contact-item">
        <svg class="contact-icon" viewBox="0 0 24 24" aria-hidden="true">
          <path d="M2 8c0-2 3-4 10-4s10 2 10 4v2h-5V8.5c-1.5-.6-3-.8-5-.8s-3.5.2-5 .8V10H2z"/>
          <path d="M6 11h12l2 9H4z"/>
        </svg>
        <span>905.555.0142</span>
      </li>
      <li class="contact-item">
        <svg class="contact-icon" viewBox="0 0 24 24" aria-hidden="true">
          <path d="M2 6h20v13H2z M3.5 7.5l8.5 6.5 8.5-6.5" stroke="#fff" stroke-width="1.5"/>
        </svg>
        <span>info@lumagrin.com</span>
      </li>
      <li class="contact-item">
        <svg class="contact-icon" viewBox="0 0 24 24" aria-hidden="true">
          <circle cx="12" cy="12" r="10"/>
          <path d="M7 6c2 1 3 2 2 4s-3 1-3 3 2 3 1 5M15 5c-1 2 1 3 3 3M14 14c2 0 3 2 2 5" stroke="#fff" stroke-width="1.6" fill="none"/>
        </svg>
        <span>www.lumagrin.com</span>
      </li>
    </ul>

    <address class="address">
      48 Maple Crest Road,<br>
      Aurora, ON L4G 3K7
    </address>

    <svg class="footer-band" viewBox="0 0 742 13" preserveAspectRatio="none" aria-hidden="true">
      <polygon points="0,0 374,0 366,13 0,13" fill="var(--brand-maroon)"/>
      <polygon points="380,0 742,0 742,13 372,13" fill="var(--band-grey)"/>
    </svg>
  </section>
</body>
</html>
```